Business card (AI file uploaded)

We need a business card design that is minimalist using existing logo (attached). Source files must be editable so we can make the same design with other names.

Screenshots included of a design I was working on to give you an idea of the style I would like. Looking for similar modern styles

Thanks

```html
<!DOCTYPE html>
<html lang="en">
<head>
<meta charset="utf-8">
<title>Marlow Law Group – Business Card</title>
<link rel="stylesheet" href="https://fonts.googleapis.com/css2?family=Open+Sans:wght@400;600;700&display=swap">
<style>
  :root {
    --page-bg: #d4d4d4;
    --card-light: #f3f3f3;
    --card-light-edge: #e4e4e4;
    --ink-dark: #2f2f2f;
    --ink-mid: #4a4a4a;
    --band-dark: #3b3b3b;
    --band-grey: #c4c4c4;
    --divider: #cfcfcf;
    --white: #ffffff;
  }
  * { box-sizing: border-box; margin: 0; padding: 0; }
  html, body { width: 1200px; height: 894px; overflow: hidden; }
  body {
    background: var(--page-bg);
    font-family: "Open Sans", Arial, sans-serif;
    position: relative;
  }
  .card {
    position: absolute;
    left: 300px;
    width: 600px;
    height: 343px;
    border-radius: 4px;
    overflow: hidden;
    box-shadow: 0 6px 18px rgba(0,0,0,0.18);
  }
  .card--front { top: 64px; background: linear-gradient(135deg, var(--white), var(--card-light) 60%, var(--card-light-edge)); }
  .card--back { top: 468px; background: var(--band-dark); }

  /* front: contact side */
  .side-band { position: absolute; left: 0; top: 0; width: 70px; height: 343px; }
  .contact-list {
    position: absolute; left: 84px; top: 58px;
    list-style: none; color: var(--ink-mid);
    font-size: 15px; line-height: 25px;
  }
  .person { position: absolute; left: 84px; top: 248px; }
  .person__name { font-size: 17px; font-weight: 700; color: var(--ink-dark); }
  .person__title { font-size: 13px; color: var(--ink-mid); margin-top: 2px; }

  .divider {
    position: absolute; left: 318px; top: 40px; width: 1px; height: 263px;
    background: linear-gradient(var(--card-light), var(--divider) 30%, var(--divider) 70%, var(--card-light));
  }

  /* front: brand side */
  .brand { position: absolute; display: flex; align-items: center; gap: 10px; }
  .brand__dot { border-radius: 50%; flex: none; }
  .brand__name { font-weight: 600; text-transform: uppercase; letter-spacing: 1px; line-height: 1.05; }
  .card--front .brand { left: 344px; top: 70px; }
  .card--front .brand__dot { width: 40px; height: 40px; border: 3px solid var(--ink-dark); }
  .card--front .brand__name { font-size: 22px; color: var(--ink-dark); }

  .address { position: absolute; left: 344px; top: 178px; font-size: 14px; line-height: 21px; color: var(--ink-dark); }
  .website { position: absolute; left: 344px; top: 240px; font-size: 14px; font-weight: 700; letter-spacing: 1.5px; color: var(--ink-dark); }

  /* back */
  .card--back .brand { left: 50%; top: 50%; transform: translate(-50%, -50%); }
  .card--back .brand__dot { width: 52px; height: 52px; border: 3px solid var(--white); }
  .card--back .brand__name { font-size: 30px; color: var(--white); }
  .back-tab { position: absolute; right: 0; width: 18px; height: 62px; background: #e6e6e6; border-radius: 6px 0 0 6px; }
  .back-tab--top { top: 30px; }
  .back-tab--bottom { bottom: 30px; }
</style>
</head>
<body>
  <section class="card card--front" aria-label="Business card front">
    <svg class="side-band" viewBox="0 0 70 343" aria-hidden="true">
      <path d="M0 0 H40 V150 Q40 170 60 174 H70 V343 H0 Z" fill="var(--band-grey)"/>
      <path d="M0 0 H58 V128 Q58 150 36 154 H0 Z" fill="var(--band-dark)"/>
      <!-- phone -->
      <path d="M24 64 q2 -3 5 -1 l3 3 q1 2 -1 3 l-1 1 q1 3 4 5 l1 -1 q2 -1 3 1 l3 3 q1 3 -2 4 q-6 1 -12 -6 q-5 -6 -3 -12 z" fill="var(--white)"/>
      <!-- mobile -->
      <rect x="25" y="90" width="12" height="19" rx="2" fill="none" stroke="var(--white)" stroke-width="2"/>
      <!-- mail -->
      <rect x="23" y="118" width="17" height="12" fill="none" stroke="var(--white)" stroke-width="2"/>
      <path d="M23 118 L31.5 125 L40 118" fill="none" stroke="var(--white)" stroke-width="2"/>
    </svg>
    <ul class="contact-list">
      <li>(+1) 555 014 2280</li>
      <li>(+1) 555 014 2281</li>
      <li>(+1) 555 014 2282</li>
      <li>info@marlowlaw.com</li>
    </ul>
    <div class="person">
      <p class="person__name">Daniel Hart</p>
      <p class="person__title">President and CEO</p>
    </div>
    <div class="divider"></div>
    <div class="brand">
      <span class="brand__dot"></span>
      <span class="brand__name">Marlow<br>Law Group</span>
    </div>
    <p class="address">245 Harbour Ave, Toronto ON<br>Canada M5V2K9</p>
    <p class="website">www.marlowlaw.com</p>
  </section>

  <section class="card card--back" aria-label="Business card back">
    <div class="brand">
      <span class="brand__dot"></span>
      <span class="brand__name">Marlow<br>Law Group</span>
    </div>
    <span class="back-tab back-tab--top"></span>
    <span class="back-tab back-tab--bottom"></span>
  </section>
</body>
</html>
```